Crestline Marketing Business Card

Business card using new logo for marketing consulting company based in Silicon Valley. Limited information on card now (name, phone number, email, website), but room to add mailing address later.

```html
<!DOCTYPE html>
<html lang="en">
<head>
<meta charset="utf-8">
<title>Crestline Marketing Business Card</title>
<link href="https://fonts.googleapis.com/css2?family=Ubuntu:wght@300;400;500&display=swap" rel="stylesheet">
<style>
  :root {
    --backdrop: #e4e5e8;
    --paper: #ffffff;
    --navy: #1e2b5a;
    --sky: #2db3ea;
    --grey: #8a8f99;
  }
  * { margin: 0; padding: 0; box-sizing: border-box; }
  html, body {
    width: 1037px; height: 1200px; overflow: hidden;
    background: var(--backdrop);
    font-family: "Ubuntu", Arial, sans-serif;
  }
  .card {
    position: absolute; left: 188px;
    width: 660px; height: 400px;
    background: var(--paper);
    overflow: hidden;
  }
  .card--front { top: 130px; }
  .card--back { top: 660px; background: var(--navy); }

  .brand { display: flex; flex-direction: column; align-items: center; }
  .brand__dot { border-radius: 50%; background: var(--sky); }
  .brand__name {
    color: var(--navy); font-weight: 500; text-transform: uppercase;
    text-align: center; line-height: 1.15;
  }
  .card--front .brand {
    position: absolute; left: 0; right: 0; top: 120px;
  }
  .card--front .brand__dot { width: 58px; height: 58px; margin-bottom: 18px; }
  .card--front .brand__name { font-size: 34px; letter-spacing: 1px; }

  .card__art { position: absolute; inset: 0; }
  .card--back .brand { position: absolute; left: 440px; top: 44px; width: 220px; }
  .card--back .brand__dot { width: 40px; height: 40px; margin-bottom: 12px; }
  .card--back .brand__name { font-size: 24px; }

  .person { position: absolute; left: 58px; top: 118px; }
  .person__name { color: var(--sky); font-size: 38px; font-weight: 300; text-transform: uppercase; }
  .person__role { color: var(--paper); font-size: 18px; font-weight: 400; margin-top: 4px; }

  .contact {
    position: absolute; display: flex; align-items: center; gap: 10px;
    color: var(--paper); font-size: 17px; font-weight: 400;
  }
  .contact svg { width: 18px; height: 18px; flex: none; }
  .contact--phone { left: 58px; top: 308px; }
  .contact--email { left: 58px; top: 345px; }
  .contact--web { left: 428px; top: 345px; }
</style>
</head>
<body>
  <section class="card card--front">
    <div class="brand">
      <span class="brand__dot"></span>
      <span class="brand__name">Crestline Marketing</span>
    </div>
  </section>

  <section class="card card--back">
    <svg class="card__art" viewBox="0 0 660 400" aria-hidden="true">
      <polygon points="205,0 232,0 660,292 660,312" fill="var(--sky)"/>
      <polygon points="232,0 660,0 660,292" fill="var(--paper)"/>
    </svg>
    <div class="brand">
      <span class="brand__dot"></span>
      <span class="brand__name">Crestline<br>Marketing</span>
    </div>
    <div class="person">
      <div class="person__name">Daniel Harper</div>
      <div class="person__role">manager</div>
    </div>
    <div class="contact contact--phone">
      <svg viewBox="0 0 18 18"><rect width="18" height="18" rx="4" fill="var(--sky)"/><path d="M6 4.5l2 2-1 1.2c.7 1.4 1.8 2.5 3.3 3.3l1.2-1 2 2-1.2 1.5C9 13 5 9 4.5 5.7z" fill="var(--paper)"/></svg>
      <span>000000000000000</span>
    </div>
    <div class="contact contact--email">
      <svg viewBox="0 0 18 18"><rect width="18" height="18" rx="4" fill="var(--sky)"/><rect x="4" y="5.5" width="10" height="7" fill="var(--paper)"/><path d="M4 5.5l5 4 5-4" stroke="var(--sky)" stroke-width="1" fill="none"/></svg>
      <span>dh@crestlinemkt.com</span>
    </div>
    <div class="contact contact--web">
      <svg viewBox="0 0 18 18"><rect width="18" height="18" rx="4" fill="var(--sky)"/><circle cx="9" cy="9" r="4.5" fill="none" stroke="var(--paper)" stroke-width="1.3"/><path d="M4.5 9h9M9 4.5v9" stroke="var(--paper)" stroke-width="1"/></svg>
      <span>www.crestlinemkt.com</span>
    </div>
  </section>
</body>
</html>
```